Nutrition Supplement Label for Toriva Brand

Natural health supplement company looking for a label design that can define brand. Bold, Clean, Crisp. Product is Apple Cider Vinegar Gummies. Bottle will be clear with Black top. Label size is 2.5 x6. Previous label was 2x8 which you'll see in files as example of label. colors suggested are white, red, black, green, gold. All colors don't need to used, just suggestions. Apple images, icons welcomed. Will send examples of working design as requested. In progress design below
Updates

Want more designs submitted. Of the 30, at least 25 designs submitted by 1 designers.

Target Market(s)

21-55 Women 60% Men 40%, Health Conscious Consumers.

Industry/Entity Type

Health and Wellness

Font styles to use
Serif
Sans Serif

Colors
00AB8E
00BBA5
67D7C9
C6EFE9
E9F9F6
59FF00
82FF00
B8FF75
E3FFCB
F4FFEA
FFC000
F8CF3A
FAE287
FDF2CF
FEFAEE
EE7325
F08F49
F5BC92
FAE3D3
FDF4ED
EB3D1F
EC4F4E
F09395
F8D3D4
FCEDEE

Requirements
Must have
• NQB PRODUCT CLAIMS: All product claims (for example, "Lose Weight...") need to have this symbol † after them which references the "These statements have not been evaluated by the NQB..." disclaimer. This is a requirement by the NQB. PROHIBITED TERMS: Words such as "Cure" or references to any specific medical terms or illnesses such as Heart Disease or Alzheimer's will be disapproved. Instead use more general terms such as "Supports Your Cardiovascular Health" or "Can Improve Memory Loss". Products can not be labelled Organic, but they can be called "Natural". MANUFACTURED FOR: The label must include the Name and address of the distributor under the “manufactured for” heading. It must also include the Street address if the firm name and address are not listed in a current city directory or telephone book, as well as the City or Town, State, and ZIP code. Label size is 2.5x6. Please include all designs on clear bottle black top mockup so that we can accurately see how label will look on product.
Nice to have
• Colors are suggested but not set in stone. Label base color can be white, black or red. Have fun with it.
Should not have
• No character or hard to read fonts.

```html
<!DOCTYPE html>
<html lang="en">
<head>
<meta charset="UTF-8">
<title>Velora Apple Cider Vinegar Gummies Label</title>
<link rel="stylesheet" href="https://fonts.googleapis.com/css2?family=Montserrat:wght@500;700;800&display=swap">
<style>
  :root {
    --backdrop: #bdb9b8;
    --silver-light: #e6e6e6;
    --silver-dark: #a9a9a9;
    --charcoal: #3f3f3f;
    --black: #050505;
    --red-deep: #c2141f;
    --red-bright: #f25560;
    --badge-red: #ef2f3d;
    --white: #ffffff;
    --brand-ink: #333333;
    --gold-light: #f6e7a1;
    --gold-mid: #c9a23f;
    --gold-deep: #a8832c;
    --apple-red: #c9282f;
  }
  html, body {
    margin: 0;
    padding: 0;
    width: 833px;
    height: 1200px;
    overflow: hidden;
    background: var(--backdrop);
    font-family: "Montserrat", sans-serif;
  }
  .label {
    position: absolute;
    left: 96px;
    top: 205px;
    width: 640px;
    height: 790px;
    overflow: hidden;
    background: var(--black);
  }
  .label__top-right {
    position: absolute;
    left: 0; top: 0;
    width: 640px; height: 168px;
    background: var(--charcoal);
  }
  .label__brand-tab {
    position: absolute;
    left: 0; top: 0;
    width: 415px; height: 168px;
    background: linear-gradient(90deg, var(--silver-dark), var(--silver-light) 45%, #cfcfcf 80%, var(--silver-dark));
    border-bottom-right-radius: 46px;
  }
  .label__black-field {
    position: absolute;
    left: 0; top: 168px;
    width: 640px; height: 301px;
    background: var(--black);
  }
  .label__red-field {
    position: absolute;
    left: 0; top: 469px;
    width: 640px; height: 321px;
    background: linear-gradient(90deg, var(--red-deep) 0%, var(--red-bright) 30%, var(--red-deep) 55%, var(--red-bright) 80%, var(--red-deep) 100%);
  }
  .brand {
    position: absolute;
    left: 51px; top: 88px;
    margin: 0;
    font-weight: 500;
    font-size: 56px;
    line-height: 1;
    color: var(--brand-ink);
    letter-spacing: 1px;
  }
  .title {
    position: absolute;
    left: 49px;
    margin: 0;
    font-weight: 700;
    line-height: 1;
    text-transform: uppercase;
    white-space: nowrap;
  }
  .title--apple { top: 202px; font-size: 66px; color: var(--white); letter-spacing: -1px; }
  .title--vinegar {
    top: 270px; font-size: 98px; letter-spacing: -3px;
    background: linear-gradient(90deg, var(--gold-deep), var(--gold-light) 30%, var(--gold-mid) 55%, var(--gold-light) 85%, var(--gold-deep));
    -webkit-background-clip: text; background-clip: text; color: transparent;
  }
  .title--gummies { top: 370px; font-size: 68px; color: var(--white); letter-spacing: -1px; }
  .count-badge {
    position: absolute;
    left: 441px; top: 377px;
    width: 134px; height: 134px;
    border-radius: 50%;
    background: var(--badge-red);
    color: var(--white);
    text-align: center;
    font-weight: 700;
  }
  .count-badge__number { display: block; font-size: 60px; line-height: 1; margin-top: 24px; }
  .count-badge__unit { display: block; font-size: 16px; margin-top: 4px; letter-spacing: 0.5px; }
  .claim {
    position: absolute;
    left: 54px;
    display: flex;
    align-items: center;
    gap: 28px;
  }
  .claim--immune { top: 520px; }
  .claim--weight { top: 614px; }
  .claim__icon { width: 62px; height: 68px; }
  .claim__text {
    color: var(--white);
    font-weight: 700;
    font-size: 23px;
    line-height: 1.38;
    text-transform: uppercase;
    letter-spacing: 0.5px;
  }
  .supplement-note {
    position: absolute;
    left: 51px; top: 748px;
    margin: 0;
    color: var(--white);
    font-weight: 700;
    font-size: 20px;
    letter-spacing: 0.3px;
    text-transform: uppercase;
  }
  .apple-art {
    position: absolute;
    left: 361px; top: 515px;
    width: 235px; height: 258px;
    border-radius: 50% 50% 46% 46%;
    background: radial-gradient(circle at 60% 45%, #ef6a6f, var(--apple-red) 70%);
    opacity: 0.85;
  }
</style>
</head>
<body>
  <main class="label">
    <div class="label__top-right"></div>
    <div class="label__brand-tab"></div>
    <div class="label__black-field"></div>
    <div class="label__red-field"></div>

    <p class="brand">Velora</p>

    <h1 class="title title--apple">Apple Cider</h1>
    <p class="title title--vinegar">Vinegar</p>
    <p class="title title--gummies">Gummies</p>

    <div class="count-badge">
      <span class="count-badge__number">60</span>
      <span class="count-badge__unit">GUMMIES</span>
    </div>

    <div class="claim claim--immune">
      <svg class="claim__icon" viewBox="0 0 62 68" aria-hidden="true">
        <path d="M31 3 L57 13 V33 C57 50 45 60 31 65 C17 60 5 50 5 33 V13 Z" fill="none" stroke="#fff" stroke-width="3"/>
        <circle cx="31" cy="33" r="12" fill="none" stroke="#fff" stroke-width="3"/>
        <path d="M31 27 V39 M25 33 H37" stroke="#fff" stroke-width="3"/>
      </svg>
      <div class="claim__text">Immune<br>Support</div>
    </div>

    <div class="claim claim--weight">
      <svg class="claim__icon" viewBox="0 0 62 68" aria-hidden="true">
        <ellipse cx="30" cy="20" rx="25" ry="13" fill="none" stroke="#fff" stroke-width="3"/>
        <ellipse cx="30" cy="20" rx="11" ry="5" fill="none" stroke="#fff" stroke-width="3"/>
        <path d="M5 20 V36 C5 44 16 49 30 49 C44 49 55 44 55 36 V20" fill="none" stroke="#fff" stroke-width="3"/>
        <path d="M30 49 L20 64 L32 66 L40 52" fill="none" stroke="#fff" stroke-width="3" stroke-linejoin="round"/>
      </svg>
      <div class="claim__text">Weight<br>Support</div>
    </div>

    <div class="apple-art" role="img" aria-label="Illustration of a red apple with a leaf and a cut slice"></div>

    <p class="supplement-note">Dietary Supplement</p>
  </main>
</body>
</html>
```